Candle Rental Business seeks new website design

We need a new website design for a Candle hire business. The business rents out pillar candles for events such as weddings and corporate events. Our main target market is weddings. The business name is Lease a Lantern. The business name does not have a logo design.

We would like a website that is light in colours and creates a warm atmosphere. The design needs to be elegant and upmarket. There are different size candles that we hire out, ranging from 10cm diameter to 20cm diameter, flat, tall etc. All our candles are white in colour. Its just the size that differs.

We would also like to include a section for hiring out decor such as glassvases, candlebras, overlays and chairs sachets, chair covers. However, this is not the businesses main focus but an additional offering to customers.

Target Market(s)

Wedding venues and brides. Corporate events. School dances.

Industry/Entity Type

Hospitality

Logo Text

Lease a Lantern

Number of Pages Required

1 page

Font styles to use
Sans Serif
Script

Requirements
Must have
• Pictures of pillar candles. Plain white candles. The website must centre around candles.
Nice to have
• Different examples of candle centrepieces
Should not have
• Pictures must not be of brides. Pictures of surrounding is perferable.

```html
<!DOCTYPE html>
<html lang="en">
<head>
<meta charset="utf-8">
<title>Lease a Lantern</title>
<link rel="stylesheet" href="https://fonts.googleapis.com/css2?family=Cinzel:wght@400;700&family=Open+Sans:wght@400;600&display=swap">
<style>
:root{
  --linen:#ddd5c6;
  --panel:#ffffff;
  --ink:#1f1f1f;
  --muted:#555;
  --gold:#f5c400;
  --footer:#000000;
  --overlay:rgba(20,16,12,.72);
}
*{box-sizing:border-box;margin:0;padding:0}
html,body{width:1200px;height:2848px;overflow:hidden}
body{background:var(--linen);font-family:'Open Sans',sans-serif;color:var(--ink);position:relative}
.brand{position:absolute;top:82px;left:0;width:1200px;text-align:center;font-family:'Cinzel',serif;font-weight:700;font-size:40px;letter-spacing:1px}
.panel{position:absolute;left:116px;top:152px;width:966px;height:2630px;background:var(--panel)}
.nav{position:absolute;top:42px;left:13px;right:13px;display:flex;justify-content:space-between;font-family:'Cinzel',serif;font-size:29px;font-weight:700}
.nav a{color:var(--ink);text-decoration:none;padding:0 16px 22px}
.nav a.active{border-bottom:5px solid var(--gold)}
.hero{position:absolute;left:13px;top:114px;width:942px;height:554px;background:radial-gradient(ellipse at 50% 30%,#6b5a3a 0%,#3a3024 45%,#1c1812 100%)}
.hero h1{position:absolute;top:238px;width:100%;text-align:center;font-family:'Cinzel',serif;font-weight:400;font-size:58px;color:#fff}
.dots{position:absolute;display:flex;gap:10px}
.dots span{width:12px;height:12px;border-radius:50%;background:#fff}
.dots span.on{background:var(--gold)}
.dots.grey span{background:#bbb}
.dots.grey span.on{background:var(--gold)}
.kicker{position:absolute;top:744px;width:100%;text-align:center;font-family:'Cinzel',serif;font-size:28px}
.section-title{position:absolute;width:100%;text-align:center;font-family:'Cinzel',serif;font-weight:700;font-size:36px}
.event{position:absolute;top:853px;width:458px;height:455px}
.event .label{position:absolute;left:82px;top:146px;width:292px;height:150px;background:var(--overlay);border-bottom:7px solid var(--gold);display:flex;align-items:center;justify-content:center;text-align:center;color:#fff;font-family:'Cinzel',serif;font-weight:700;font-size:28px;line-height:1.25}
.product{position:absolute;top:1466px;width:298px}
.product .photo{height:237px;position:relative}
.product h3{font-family:'Cinzel',serif;font-weight:700;font-size:20px;margin-top:14px}
.product p{font-size:13px;line-height:1.7;color:var(--muted);margin-top:6px}
.rent-btn{position:absolute;left:99px;top:101px;width:99px;height:34px;background:var(--gold);color:#fff;font-family:'Cinzel',serif;font-size:11px;display:flex;align-items:center;justify-content:center}
.decor{position:absolute;top:1941px;width:298px;height:296px}
.decor .caption{position:absolute;left:0;right:0;bottom:0;height:68px;background:rgba(20,20,20,.7);color:#fff;font-family:'Cinzel',serif;font-weight:700;font-size:20px;display:flex;align-items:center;justify-content:center}
.partners{position:absolute;top:2348px;left:40px;right:40px;display:flex;justify-content:space-between;align-items:center;font-family:'Cinzel',serif;font-size:22px;color:#333}
.footer{position:absolute;left:0;bottom:0;width:966px;height:165px;background:var(--footer);color:#fff;text-align:center}
.social{position:absolute;top:34px;left:0;width:100%;display:flex;justify-content:center;gap:14px}
.social span{width:16px;height:16px;border-radius:50%;background:#fff}
.footer-nav{position:absolute;top:72px;width:100%;font-family:'Cinzel',serif;font-size:13px;font-weight:700;letter-spacing:.5px}
.copyright{position:absolute;top:110px;width:100%;font-family:'Cinzel',serif;font-size:12px;font-weight:700}
</style>
</head>
<body>
<div class="brand">Lease a Lantern</div>
<main class="panel">
  <nav class="nav">
    <a class="active">Home</a><a>About Us</a><a>Products</a><a>Location</a><a>Contact Us</a>
  </nav>
  <section class="hero" role="img" aria-label="Candlelit banquet hall with string lights and set tables">
    <h1>Lease a Lantern</h1>
    <div class="dots" style="left:440px;top:503px"><span class="on"></span><span></span><span></span></div>
  </section>

  <div class="kicker">We rent out</div>
  <h2 class="section-title" style="top:776px">Pillar Candles for Events</h2>

  <div class="event" style="left:13px;background:linear-gradient(135deg,#c98a6a,#7a4a3a 50%,#3a2a24)" role="img" aria-label="Guests celebrating at a wedding party">
    <div class="label">Weddings<br>Events</div>
  </div>
  <div class="event" style="left:497px;background:linear-gradient(180deg,#c9b8a4,#8a7a8a 50%,#dcd8e0)" role="img" aria-label="Ballroom set up for a corporate event">
    <div class="label">Corporate<br>Events</div>
  </div>

  <h2 class="section-title" style="top:1376px">Our Products</h2>

  <div class="product" style="left:13px">
    <div class="photo" style="background:radial-gradient(ellipse at 50% 40%,#c98a3a,#5a3416 55%,#1a0e06)" role="img" aria-label="Rows of lit taper candles"><div class="rent-btn">Rent Now</div></div>
    <h3>Candels</h3>
    <p>Neque porro quisquam est qui dolorem ipsum quia dolor sit amet, consectetur, adipisci velit...</p>
  </div>
  <div class="product" style="left:334px">
    <div class="photo" style="background:radial-gradient(ellipse at 40% 40%,#e8c890,#a8784a 55%,#5a3a20)" role="img" aria-label="Candelabra with white candles and pillar candles"></div>
    <h3>Candels</h3>
    <p>Neque porro quisquam est qui dolorem ipsum quia dolor sit amet, consectetur, adipisci velit...</p>
  </div>
  <div class="product" style="left:659px">
    <div class="photo" style="background:linear-gradient(180deg,#f4f2ee,#dedad2 70%,#b8a8b8)" role="img" aria-label="White pillar candles on a light table"></div>
    <h3>Candels</h3>
    <p>Neque porro quisquam est qui dolorem ipsum quia dolor sit amet, consectetur, adipisci velit...</p>
  </div>

  <h2 class="section-title" style="top:1852px">Hiring Out Decor</h2>

  <div class="decor" style="left:13px;background:linear-gradient(160deg,#b8bcb0,#6a7060 60%,#2e3028)" role="img" aria-label="Yellow tulips in a glass vase"><div class="caption">Glassvases</div></div>
  <div class="decor" style="left:334px;background:radial-gradient(ellipse at 50% 30%,#6a6458,#2a2a28 60%,#141414)" role="img" aria-label="Brass candlesticks with lit candles"><div class="caption">Candlebras</div></div>
  <div class="decor" style="left:659px;background:radial-gradient(ellipse at 50% 35%,#8a8070,#4a4238 60%,#2a241e)" role="img" aria-label="Silver candelabrum with blue candles"><div class="caption">Overlays</div></div>

  <div class="dots grey" style="left:465px;top:2260px"><span></span><span></span><span class="on"></span></div>

  <div class="partners">
    <span>Wick &amp; Hope</span>
    <span>Fernlight</span>
    <span>Harbor Wick</span>
    <span>Ember Reclaim</span>
    <span>Blue Ridge Wax</span>
  </div>

  <footer class="footer">
    <div class="social"><span></span><span></span><span></span></div>
    <div class="footer-nav">Home &nbsp;| &nbsp;About Us &nbsp;| &nbsp;Products &nbsp;| &nbsp;Location &nbsp;| &nbsp;Contact Us</div>
    <div class="copyright">© 2016 Company Name | All Rights Reserved</div>
  </footer>
</main>
</body>
</html>
```